'Rebalancing Tomorrow' is a political thriller novel

I need a book cover for a political thriller. The book is about a presidential campaign in 2024. A politician has a revolutionary new idea on how to move the economy from growing on debt based to thriving in abundance. A billionaire oil (Varn) family undermines his campaign with blistering negative adds. A technology billionaire attempts to assassinate him. But ultimately the incumbent president seeking a third term will not give up power...
There is an underlying theory of economics told that is meant to educate the reader about how the majority of Americans and people around the world are trying to get by in a rigged system. Although the majority of people are much worse of then they need to be the truth is nobody is winning with the current economy (unless there sinister motivations involved). The story makes dire predictions of a technological dystopia.
Updates
Author's name: Odd Brekke
Reason: There are so many very good choices but I haven't found the perfect one yer.
Target Market(s)
Anyone who is interested in living in a better world and changing what is not working and clearly getting worse.
Industry/Entity Type
Political
Colors
Designer to choose colors to be used in the design.
Look and feel
Each slider illustrates characteristics of the customer's brand and the style your logo design should communicate.

```html
<!DOCTYPE html>
<html lang="en">
<head>
<meta charset="utf-8">
<title>Rebalancing Tomorrow — Odd Brekke</title>
<link rel="stylesheet" href="https://fonts.googleapis.com/css2?family=Cinzel:wght@400;500&family=League+Gothic&display=swap">
<style>
  :root {
    --night: #07121c;
    --deep-blue: #0d2a3d;
    --steel-blue: #2b5a74;
    --haze-blue: #5d8aa3;
    --ink-white: #ffffff;
    --reticle: rgba(235, 245, 255, 0.75);
    --gold-light: #ffe07a;
    --gold-mid: #e0a81c;
    --gold-dark: #9a6a08;
    --flag-red: #b3262e;
    --flag-navy: #1c2c52;
    --flag-white: #e9e6e2;
  }
  * { margin: 0; padding: 0; box-sizing: border-box; }
  html, body {
    width: 752px;
    height: 1200px;
    overflow: hidden;
    background: var(--night);
  }
  .cover {
    position: relative;
    width: 752px;
    height: 1200px;
    overflow: hidden;
    background: var(--night);
  }
  .backdrop {
    position: absolute;
    inset: 0;
    background:
      radial-gradient(ellipse 420px 300px at 380px 300px, rgba(93,138,163,0.75), transparent 70%),
      linear-gradient(180deg, var(--deep-blue) 0%, var(--steel-blue) 22%, var(--haze-blue) 34%, var(--deep-blue) 52%, var(--night) 78%, var(--night) 100%);
  }
  .reticle {
    position: absolute;
    inset: 0;
    width: 752px;
    height: 1200px;
  }
  .author {
    position: absolute;
    top: 40px;
    left: 0;
    width: 752px;
    text-align: center;
    font-family: "Cinzel", serif;
    font-weight: 400;
    font-size: 62px;
    letter-spacing: 0.18em;
    color: var(--ink-white);
    text-indent: 0.18em;
    line-height: 1;
  }
  .gold-bars {
    position: absolute;
    left: 180px;
    top: 292px;
    width: 394px;
    height: 292px;
    background: linear-gradient(150deg, var(--gold-light) 0%, var(--gold-mid) 45%, var(--gold-dark) 100%);
    clip-path: polygon(0 55%, 55% 8%, 80% 20%, 100% 45%, 100% 75%, 62% 100%, 10% 82%);
  }
  .title {
    position: absolute;
    left: 0;
    top: 0;
    width: 752px;
    height: 1200px;
  }
  .title text {
    font-family: "League Gothic", "Oswald", sans-serif;
    fill: var(--ink-white);
  }
  .flag {
    position: absolute;
    left: 0;
    bottom: 0;
    width: 752px;
    height: 250px;
    background:
      linear-gradient(100deg, var(--flag-navy) 0%, var(--flag-navy) 28%, var(--flag-white) 34%, var(--flag-red) 45%, var(--flag-white) 58%, var(--flag-red) 72%, var(--flag-red) 100%);
    clip-path: polygon(0 22%, 30% 30%, 55% 40%, 75% 20%, 100% 8%, 100% 100%, 0 100%);
    opacity: 0.9;
  }
  .vote-button {
    position: absolute;
    left: 508px;
    top: 944px;
    width: 202px;
    height: 202px;
    border-radius: 50%;
    background: radial-gradient(circle at 40% 35%, var(--flag-white) 0%, #c8c6c4 45%, var(--flag-navy) 72%, var(--flag-red) 100%);
  }
</style>
</head>
<body>
<div class="cover">
  <div class="backdrop" role="img" aria-label="Dark blue photograph of the Capitol dome at dusk with city lights below"></div>

  <svg class="reticle" viewBox="0 0 752 1200" aria-hidden="true">
    <circle cx="376" cy="454" r="316" fill="none" stroke="var(--reticle)" stroke-width="1.5"/>
    <line x1="376" y1="0" x2="376" y2="770" stroke="var(--reticle)" stroke-width="1"/>
    <line x1="0" y1="454" x2="752" y2="454" stroke="var(--reticle)" stroke-width="1"/>
  </svg>

  <div class="gold-bars" role="img" aria-label="Stack of shiny fine gold bars"></div>

  <div class="author">ODD BREKKE</div>

  <svg class="title" viewBox="0 0 752 1200" role="heading" aria-level="1" aria-label="Rebalancing Tomorrow">
    <text x="120" y="633" font-size="152" textLength="512" lengthAdjust="spacingAndGlyphs">REBALANCING</text>
    <text x="54" y="943" font-size="373" textLength="644" lengthAdjust="spacingAndGlyphs">TOMORROW</text>
  </svg>

  <div class="flag" role="img" aria-label="Waving American flag along the bottom edge"></div>
  <div class="vote-button" role="img" aria-label="Round campaign vote pin button"></div>
</div>
</body>
</html>
```